New Website for ReBranded Company - CrewBeacon

We have a successful company and website currently but it is a little dated. We have re-branded the company from Harbor Signal Networks to CrewBeacon and have a new logo for the new name. We are looking to build a newer fresher website with the new name. I will need a concept of the home page and one inside page. You can see our current site at https://www.harborsignalnetworks.example and the new site will be https://www.crewbeacon.example .

I also really like the https://www.pathlantern.example/ website. I like ledgerkite.example website. I like the https://skillorbit.example/ website.

See the attached document for layout and some text to use. Use the pictures I attached as opposed to pictures from the old site as much as you can.

Target Market(s)

Business

Industry/Entity Type

Software Service

Number of Pages Required

2 page

Font styles to use
Sans Serif

Requirements
Must have
• Use the colors from my logo. Professional but modern. We want people to feel like our product makes their staff feel safer at work.
Should not have
• Don't use any red or orange (no stop colors).

```html
<!DOCTYPE html>
<html lang="en">
<head>
<meta charset="utf-8">
<title>CrewBeacon — Smart Safety Solutions</title>
<link rel="stylesheet" href="https://fonts.googleapis.com/css2?family=Poppins:wght@600;700&family=Rubik:wght@300;400;500;600&display=swap">
<style>
:root{
  --brand:#2f8fd0;
  --brand-dark:#1f6fa8;
  --green:#22b573;
  --ink:#1d1d1f;
  --text:#444;
  --muted:#666;
  --light:#f7f7f7;
  --sand:#e2d7c5;
  --footer:#3569d4;
  --white:#fff;
}
*{margin:0;padding:0;box-sizing:border-box}
html,body{width:1200px;height:4662px;overflow:hidden}
body{font-family:'Rubik',sans-serif;color:var(--text);background:var(--white);position:relative}
.abs{position:absolute}
.photo{position:absolute}
a{color:inherit;text-decoration:none}

/* header */
.site-header{position:absolute;left:0;top:0;width:1200px;height:76px;background:var(--white)}
.brand{position:absolute;left:100px;top:20px;display:flex;align-items:center;gap:10px;font-family:'Rubik',sans-serif;font-weight:500;font-size:25px;color:var(--brand)}
.brand .dot{width:30px;height:30px;border-radius:50%;background:var(--brand)}
.main-nav{position:absolute;left:447px;top:31px;display:flex;gap:30px;font-size:11.5px;font-weight:500;color:var(--ink);letter-spacing:.3px}
.header-tools{position:absolute;left:1054px;top:28px;display:flex;gap:14px}

/* hero */
.hero{position:absolute;left:7px;top:76px;width:1186px;height:469px;background:linear-gradient(100deg,#2d3a33 0%,#4a5750 45%,#6f7a72 70%,#3d4541 100%)}
.hero-eyebrow{position:absolute;left:99px;top:180px;color:#e8e8e8;font-size:16px;text-transform:uppercase}
.hero-title{position:absolute;left:99px;top:208px;font-family:'Poppins',sans-serif;font-weight:700;font-size:48px;line-height:54px;color:var(--white)}
.hero-text{position:absolute;left:99px;top:338px;width:560px;font-size:12.5px;line-height:24px;color:#f0f0f0}
.btn{position:absolute;display:flex;align-items:center;justify-content:center;font-size:12px;font-weight:500;letter-spacing:.8px;text-transform:uppercase;border-radius:24px}
.btn-green{background:var(--green);color:var(--white)}
.btn-outline{border:2px solid var(--brand);color:var(--brand)}
.btn-ghost{border:2px solid var(--white);color:var(--white)}

/* protected */
.protect{position:absolute;left:7px;top:545px;width:1186px;height:720px;background:var(--light)}
.section-title{position:absolute;left:0;width:1200px;text-align:center;color:var(--ink)}
.protect-title{top:612px;font-size:32px;font-weight:500;text-transform:uppercase}
.protect-title u{text-underline-offset:5px;text-decoration-thickness:2px}
.protect-sub{top:667px;font-size:14px;letter-spacing:.6px;color:var(--ink)}
.feature{position:absolute;left:98px;width:470px}
.feature svg{position:absolute;left:0;top:0}
.feature h3{position:absolute;left:83px;top:0;font-size:18px;font-weight:500;color:var(--ink)}
.feature p{position:absolute;left:83px;top:36px;width:380px;font-size:12.5px;line-height:22px;color:var(--text)}

/* why */
.why{position:absolute;left:7px;top:1265px;width:1186px;height:534px;background:var(--sand)}
.eyebrow{font-size:12.5px;letter-spacing:1.2px;text-transform:uppercase;color:var(--ink)}
.why-title{position:absolute;left:528px;top:1364px;font-size:35px;font-weight:500;color:var(--ink);text-transform:uppercase}
.why-text{position:absolute;left:528px;top:1416px;width:560px;font-size:12.5px;line-height:25px;color:var(--text)}
.tabs{position:absolute;left:528px;top:1516px;display:flex;align-items:center;gap:20px;font-size:11.5px;font-weight:500;color:var(--ink);text-transform:uppercase}
.tabs .active{background:var(--brand);color:var(--white);border-radius:20px;padding:11px 18px}

/* worry */
.worry-head{position:absolute;left:99px;top:1885px;width:400px;font-size:34px;font-weight:500;line-height:55px;color:var(--ink)}
.worry-sub{position:absolute;left:99px;top:2096px;width:400px;font-size:23px;font-weight:500;line-height:39px;color:var(--ink)}
.operating{top:2332px;font-size:22px;font-weight:500}
.operating u{text-underline-offset:5px}
.stat{position:absolute;top:2412px;width:240px}
.stat svg{position:absolute;left:0;top:4px}
.stat .num{position:absolute;left:52px;top:0;font-size:42px;font-weight:400;color:var(--ink);line-height:46px}
.stat .label{position:absolute;left:52px;top:58px;font-size:12.5px;color:var(--text)}

/* plan */
.plan{position:absolute;left:7px;top:2552px;width:1186px;height:646px;background:var(--light)}
.plan-title{top:2668px;font-size:33px;font-weight:500;text-transform:uppercase}
.step{position:absolute;top:2740px;width:326px;text-align:center}
.step .photo{left:0;top:0;width:326px;height:239px}
.step h3{position:absolute;top:262px;width:326px;font-size:17px;font-weight:500;color:var(--ink)}
.step p{position:absolute;top:298px;width:326px;font-size:12.5px;line-height:21px;color:var(--text)}

/* video */
.video{position:absolute;left:7px;top:3198px;width:1186px;height:487px;background:linear-gradient(160deg,#2b2a28 0%,#4a4843 50%,#2a2825 100%)}
.video-eyebrow{top:3328px;color:#e6e6e6;font-size:12.5px;letter-spacing:1.2px;text-transform:uppercase}
.video-title{top:3356px;color:var(--white);font-family:'Poppins',sans-serif;font-weight:600;font-size:30px}

/* testimonials */
.testi-title{top:3792px;font-size:36px;font-weight:500}
.quote{position:absolute;top:3870px;width:318px;height:230px;background:var(--white);box-shadow:0 2px 10px rgba(0,0,0,.07);text-align:center}
.quote .avatar{position:absolute;left:84px;top:22px;width:52px;height:52px;border-radius:50%}
.quote .name{position:absolute;left:150px;top:40px;font-size:13px;font-weight:500;color:var(--ink);text-align:left}
.quote p{position:absolute;left:28px;top:98px;width:262px;font-size:12.5px;line-height:25px;color:var(--text)}

/* footer */
.site-footer{position:absolute;left:0;top:4226px;width:1200px;height:436px;background:var(--footer);color:var(--white)}
.fcol{position:absolute;top:82px}
.fcol h4{font-size:16px;font-weight:500;margin-bottom:22px}
.fcol li{list-style:none;font-size:12.5px;line-height:31px}
.fcol p{font-size:12.5px;line-height:22px}
.fcol strong{font-weight:600}
.footer-brand{position:absolute;left:92px;top:257px;width:218px;height:76px;background:var(--white);display:flex;align-items:center;justify-content:center;gap:10px;color:var(--brand);font-size:25px;font-weight:500}
.footer-brand .dot{width:28px;height:28px;border-radius:50%;background:var(--brand)}
.legal{position:absolute;left:92px;top:396px;display:flex;gap:22px;font-size:11.5px}
.legal .ul{text-decoration:underline}
.copy{position:absolute;right:94px;top:396px;font-size:11px}
</style>
</head>
<body>

<header class="site-header">
  <a class="brand" href="#"><span class="dot"></span>CrewBeacon</a>
  <nav class="main-nav">
    <a href="#">HOME</a><a href="#">INDUSTRIES</a><a href="#">CASE STUDIES</a><a href="#">BUY ADDONS</a><a href="#">CONTACT</a><a href="#">BLOG</a><a href="#">LOGIN</a>
  </nav>
  <div class="header-tools">
    <svg width="16" height="16" viewBox="0 0 16 16" fill="none" stroke="#1d1d1f" stroke-width="2"><circle cx="6.5" cy="6.5" r="5"/><path d="M10.5 10.5l4 4"/></svg>
    <svg width="16" height="16" viewBox="0 0 16 16" stroke="#1d1d1f" stroke-width="2"><path d="M2 4h12M2 8h12M2 12h12"/></svg>
  </div>
</header>

<section class="hero" role="img" aria-label="Hand pressing a panic button mounted under a desk"></section>
<p class="hero-eyebrow">We gathered the most talented experts</p>
<h1 class="hero-title">Provide Smart<br>Safety Solutions</h1>
<p class="hero-text">Lorem Ipsum is simply dummy text of the printing and typesetting industry. Lorem Ipsum has been the industry's standard dummy text ever since.</p>
<a class="btn btn-green" href="#" style="left:105px;top:413px;width:176px;height:43px">Discover More</a>

<section class="protect"></section>
<h2 class="section-title protect-title">Feel <u>confident</u> that your staff is protected</h2>
<p class="section-title protect-sub">Get a revolutionary new electronic panic button</p>

<div class="feature" style="top:758px">
  <svg width="42" height="42" viewBox="0 0 42 42" fill="#2f8fd0"><path d="M12 4l8 4v8l-8 4-8-4V8z"/><path d="M30 4l8 4v8l-8 4-8-4V8z" opacity=".8"/><path d="M21 20l8 4v8l-8 4-8-4v-8z" opacity=".9"/></svg>
  <h3>Precaution</h3>
  <p>Problems Stopped Before They Start For Any Type Of Organization</p>
</div>
<div class="feature" style="top:877px">
  <svg width="42" height="42" viewBox="0 0 42 42"><path d="M15 6h12l-3 7h-6z" fill="#2f8fd0"/><rect x="6" y="13" width="30" height="26" rx="10" fill="#2f8fd0"/><text x="21" y="32" text-anchor="middle" font-family="Rubik,sans-serif" font-size="15" font-weight="600" fill="#fff">$</text></svg>
  <h3>Affordable</h3>
  <p>Affordable Prices Starting at $18 per month. No Contracts. No Hidden Costs.</p>
</div>
<div class="feature" style="top:996px">
  <svg width="42" height="42" viewBox="0 0 42 42" fill="none" stroke="#2f8fd0" stroke-width="2"><circle cx="21" cy="24" r="11"/><path d="M21 18v7M21 28v2M21 4v5M8 9l3 3M34 9l-3 3M4 20h4M34 20h4"/></svg>
  <h3>Alerts</h3>
  <p>Alerts by computer, mobile device, text, phone, email, monitoring and E911</p>
</div>
<a class="btn btn-outline" href="#" style="left:177px;top:1129px;width:248px;height:43px">Ready to get started</a>
<div class="photo" role="img" aria-label="Person taking a panic button out of a jeans pocket" style="left:586px;top:731px;width:503px;height:378px;background:linear-gradient(135deg,#2c4a73 0%,#1f3a5e 55%,#3b5a86 100%)"></div>

<section class="why"></section>
<div class="photo" role="img" aria-label="Panic button units with cables laid out on a table" style="left:28px;top:1300px;width:425px;height:470px;background:radial-gradient(ellipse at 50% 50%,#6a5d4f 0%,#a49683 45%,#e2d7c5 75%)"></div>
<p class="abs eyebrow" style="left:528px;top:1337px">Things are good enough</p>
<h2 class="why-title">Why businesses choose us</h2>
<p class="why-text">Fusce id nisi arcu. Donec ac mauris imperdiet felis efficitur the lacinia. Nam eu cursus felis.Donec ac mauris imperdiet felis efficitur the lacinia. Nam eu cursus felis. efficitur the lacinia.</p>
<div class="tabs"><span class="active">Easy to use</span><span>Communicate the way you want</span><span style="margin-left:16px">Cost effective protection</span></div>
<p class="why-text" style="top:1574px">Press a button and let the right people know you need help and open a chat window letting everyone talk on resolving their problem.</p>
<a class="btn btn-outline" href="#" style="left:528px;top:1658px;width:248px;height:43px">Ready to get started</a>

<h2 class="worry-head">We know how scary it can feel to worry about employee safety.</h2>
<p class="worry-sub">That's why we have provided a way for customers to get help to staff effectively.</p>
<div class="photo" role="img" aria-label="Desk phone with a panic button beside it on an office desk" style="left:514px;top:1864px;width:600px;height:379px;background:linear-gradient(120deg,#8a9189 0%,#5d6a63 40%,#2a2b2c 75%,#3c3a37 100%)"></div>

<h2 class="section-title operating"><u>We are successfully operating in</u></h2>
<div class="stat" style="left:87px">
  <svg width="38" height="38" viewBox="0 0 38 38" fill="none" stroke="#999" stroke-width="2"><circle cx="19" cy="19" r="16"/><path d="M19 9v10l7 4"/></svg>
  <div class="num">10</div><div class="label">Years Of Experience</div>
</div>
<div class="stat" style="left:344px">
  <svg width="38" height="38" viewBox="0 0 38 38" fill="none" stroke="#999" stroke-width="2"><circle cx="19" cy="19" r="16"/><ellipse cx="19" cy="19" rx="7" ry="16"/><path d="M3 19h32M6 11h26M6 27h26"/></svg>
  <div class="num">5</div><div class="label">Countries</div>
</div>
<div class="stat" style="left:601px">
  <svg width="38" height="38" viewBox="0 0 38 38" fill="none" stroke="#999" stroke-width="2"><rect x="3" y="8" width="32" height="24" rx="2"/><path d="M15 5h8v5h-8zM8 16h9v10H8zM21 17h9M21 22h9M21 27h6"/></svg>
  <div class="num">45</div><div class="label">States</div>
</div>
<div class="stat" style="left:856px">
  <svg width="38" height="38" viewBox="0 0 38 38" fill="none" stroke="#999" stroke-width="2"><circle cx="19" cy="19" r="16"/><circle cx="13" cy="15" r="1.5" fill="#999"/><circle cx="25" cy="15" r="1.5" fill="#999"/><path d="M11 22c4 6 12 6 16 0"/></svg>
  <div class="num">5000</div><div class="label">Happy Clients</div>
</div>

<section class="plan"></section>
<p class="section-title eyebrow" style="top:2638px">Work process</p>
<h2 class="section-title plan-title">Simple start plan</h2>
<div class="step" style="left:85px">
  <div class="photo" role="img" aria-label="Assorted panic button units on a table" style="background:radial-gradient(ellipse at 50% 50%,#8c8170 0%,#c9bfae 55%,#ddd3c2 100%)"></div>
  <h3>Explore Your Choices</h3>
  <p>Pricing<br>Trial<br>Quote<br>Hardware</p>
</div>
<div class="step" style="left:436px">
  <div class="photo" role="img" aria-label="Panic button mounted on the side of a desk" style="background:linear-gradient(90deg,#3a3d3f 0%,#6c716f 45%,#b8bcb9 70%,#5a5e5e 100%)"></div>
  <h3>Get Setup</h3>
  <p>Input Your Alerts<br>Input Your Staff<br>Install Our Software</p>
</div>
<div class="step" style="left:787px">
  <div class="photo" role="img" aria-label="Staff member carrying a panic button in a pocket" style="background:linear-gradient(135deg,#2c4a73 0%,#1f3a5e 60%,#8a948f 100%)"></div>
  <h3>Your Staff Is Protected</h3>
  <p>High Five. You just too a major step<br>to getting rid of the anxiety and<br>frustration this gave you.</p>
</div>

<section class="video" role="img" aria-label="Close-up of a panic button under a desk, video background"></section>
<p class="section-title video-eyebrow">We always stay with our clients and respect their business</p>
<h2 class="section-title video-title">Stay Connected with Staff during a Crisis Situations.</h2>
<svg class="abs" style="left:560px;top:3410px" width="80" height="80" viewBox="0 0 80 80"><circle cx="40" cy="40" r="38" fill="none" stroke="#fff" stroke-opacity=".5" stroke-width="3"/><circle cx="40" cy="40" r="31" fill="#fff"/><path d="M35 32l12 8-12 8z" fill="#1d1d1f"/></svg>
<a class="btn btn-ghost" href="#" style="left:474px;top:3528px;width:250px;height:43px">Ready to get started</a>

<p class="section-title eyebrow" style="top:3764px">Clients testimonials</p>
<h2 class="section-title testi-title">What Our Clients Say About Us</h2>
<article class="quote" style="left:98px">
  <div class="avatar" role="img" aria-label="Portrait of Elias Warrick" style="background:#c7ccd6"></div>
  <div class="name">Elias Warrick</div>
  <p>Lorem ipsum dolor sit amet, consectetur adipiscing elit. In tristique odio uthiu the augue sollicitudin venenatis. Nam volutpat nisi lorem.</p>
</article>
<article class="quote" style="left:440px">
  <div class="avatar" role="img" aria-label="Portrait of Dorian Fellowes" style="background:#b9b2aa"></div>
  <div class="name">Dorian Fellowes</div>
  <p>Lorem ipsum dolor sit amet, consectetur adipiscing elit. In tristique odio uthiu the augue sollicitudin venenatis. Nam volutpat nisi lorem.</p>
</article>
<article class="quote" style="left:782px">
  <div class="avatar" role="img" aria-label="Portrait of Mira Okonkwo" style="background:#d8d1c9"></div>
  <div class="name">Mira Okonkwo</div>
  <p>Lorem ipsum dolor sit amet, consectetur adipiscing elit. In tristique odio uthiu the augue sollicitudin venenatis. Nam volutpat nisi lorem.</p>
</article>

<footer class="site-footer">
  <div class="fcol" style="left:92px;width:230px">
    <h4>About Us</h4>
    <p>Lorem ipsum dolor sit amet, consectetur adipiscing elit. In tristique odio uthiu the augue sollicitudin venenatis. Nam volutpat nisi lorem.</p>
  </div>
  <div class="footer-brand"><span class="dot"></span>CrewBeacon</div>
  <div class="fcol" style="left:353px">
    <h4>Shop</h4>
    <ul><li>Addons</li><li>Start My Demo</li><li>Custom Quote</li><li>Start Trial</li><li>FAQ's</li></ul>
  </div>
  <div class="fcol" style="left:612px">
    <h4>About</h4>
    <ul><li>Affiliate</li><li>Contact</li><li>Support</li><li>Existing Customers</li><li>FAQ's</li><li>Blog</li></ul>
  </div>
  <div class="fcol" style="left:872px;width:240px">
    <h4>Contact Us</h4>
    <p><strong>Office Address</strong><br>1250 Lantern Ridge Dr Suite 310,<br>Maple Hollow, TN 37021</p>
    <p style="margin-top:18px"><strong>Phone:</strong> 1-800-555-0148</p>
    <p style="margin-top:18px"><strong>Email:</strong> info@crewbeacon.example</p>
  </div>
  <div class="legal"><span>Terms &amp; Conditions</span><span class="ul">Privacy Policy</span><span>End User License Agreement</span></div>
  <div class="copy">CrewBeacon - 2020</div>
</footer>

</body>
</html>
```